Verpackungsdesign für Nahrungsergänzungsmittel
Zielgruppe
Wir sind eine Firma für Nahrungsergänzungsmittel und suchen für unser neues Produkt ein Ansprechendes Etikett für die Dose. Das Produkt: GLANZ KRAFT PFLEGE
Aufgabenstellung
Deckel: weiß, geriffelt
Etikettengröße: 145 x 50 mm
Folgender Inhalt muss auf die Dose: Siehe Screenshot 0012
Außerdem soll unser Logo drauf: Siehe Bild kelvarosin.734.png
Bitte an folgenden Beispielen orientieren:
https://www.warenplatz-beispiel.example/Quelmiva-Leaf-Boost-Hochdosiert-Haar-Vitamine-N%C3%A4hrstoffe/dp/Q93318X4LP/ref=sr_1_30?__mk_de_DE=%C3%85M%C3%85%C5%BD%C3%95%C3%91&keywords=Haut+%7C+Haare+%7C+N%C3%A4gel&qid=1584445633&sr=8-30

```html
<!DOCTYPE html>
<html lang="de">
<head>
<meta charset="utf-8">
<title>Etikett – Glanz Kraft Pflege</title>
<link rel="stylesheet" href="https://fonts.googleapis.com/css2?family=Titillium+Web:wght@300;400;600;700&display=swap">
<style>
  :root{
    --green:#7ab648;
    --green-faint:#eef3e4;
    --ink:#1c1c1c;
    --text:#6b6b6b;
    --line:#c9c9c9;
    --paper:#ffffff;
  }
  *{box-sizing:border-box;margin:0;padding:0}
  html,body{width:1200px;height:474px;overflow:hidden;background:var(--paper)}
  body{font-family:"Titillium Web",sans-serif;color:var(--text)}
  .label{position:absolute;left:30px;top:40px;width:1140px;height:394px;background:var(--paper);border:1px solid #e6e6e6;overflow:hidden}
  .nutrition{position:absolute;left:40px;top:20px;width:261px;border:1px solid var(--line);font-size:10px;line-height:1.1}
  .nutrition table{width:100%;border-collapse:collapse}
  .nutrition th{background:var(--green);color:#fff;font-weight:600;text-align:left;padding:4px 3px;font-size:10px;line-height:1;vertical-align:top;height:40px}
  .nutrition th + th{text-align:right;border-left:1px solid #fff}
  .nutrition td{padding:3px;height:28px;border-top:1px solid var(--line);vertical-align:middle}
  .nutrition td + td{text-align:right;border-left:1px solid var(--line)}
  .nutrition td.tall{height:40px}
  .nutrition .notes{font-size:6px;padding:6px 3px;border-top:1px solid var(--line);line-height:1.3}
  .front{position:absolute;left:423px;top:0;width:300px;text-align:center}
  .brand{position:absolute;left:0;right:0;top:98px;display:flex;justify-content:center;align-items:center;gap:8px;font-size:22px;font-weight:400;color:var(--ink);letter-spacing:.5px}
  .brand-dot{width:14px;height:14px;border-radius:50%;background:var(--green)}
  .title{position:absolute;left:0;right:0;top:160px;font-size:44px;font-weight:700;line-height:46px;color:var(--ink)}
  .rule{position:absolute;left:55px;right:55px;top:257px;border-top:1.5px solid var(--ink)}
  .subtitle{position:absolute;left:0;right:0;top:262px;font-size:21px;letter-spacing:1px;color:var(--ink)}
  .category{position:absolute;left:0;right:0;top:297px;font-size:17px;color:#555}
  .badge{position:absolute;left:668px;top:206px;width:80px;height:80px;border-radius:50%;border:2px solid #cfcfcf}
  .band{position:absolute;left:0;right:0;top:334px;height:32px;background:var(--green);color:#fff;text-align:center;font-size:21px;letter-spacing:2px;line-height:32px}
  .info{position:absolute;left:817px;top:16px;width:310px;font-size:10.5px;line-height:1.42}
  .info p{margin-bottom:8px}
  .info b{font-weight:700}
  .maker{display:flex;gap:6px}
</style>
</head>
<body>
<main class="label">
  <section class="nutrition">
    <table>
      <tr><th>Nähr- und<br>Inhaltsstoffe</th><th>pro Tagesdosis<br>(2 Kapseln)</th><th>% NRV*</th></tr>
      <tr><td>Pantothensäure</td><td>6 mg</td><td>100%</td></tr>
      <tr><td>Vitamin B6</td><td>1,4 mg</td><td>100%</td></tr>
      <tr><td>Biotin</td><td>51 µg</td><td>100%</td></tr>
      <tr><td>Kupfer</td><td>1 mg</td><td>100%</td></tr>
      <tr><td>Zink</td><td>10 mg</td><td>100%</td></tr>
      <tr><td class="tall">Polyporus umbellatus<br>davon Polysaccharide</td><td>100 mg<br>30 mg</td><td>**</td></tr>
      <tr><td class="tall">Bambussprossen<br>—davon Silizium</td><td>43,5 mg<br>32,6 mg</td><td>**</td></tr>
    </table>
    <p class="notes">* Prozent Nährstoffbezugswerte (NRV) laut Verordnung (EU) Nr 1169/2011<br>** Keine Nährstoffbezugswerte (NRV) vorhanden</p>
  </section>

  <section class="front">
    <div class="brand"><span class="brand-dot"></span><span>KELVAROSIN</span></div>
    <h1 class="title">GLANZ KRAFT<br>PFLEGE</h1>
    <div class="rule"></div>
    <p class="subtitle">BIOTIN + ZINK</p>
    <p class="category">Nahrungsergänzungsmittel</p>
  </section>
  <div class="badge" role="img" aria-label="Herkunftssiegel"></div>

  <section class="info">
    <p><b>Zutaten:</b> Perlhirse-Extrakt 4:1, Trennmittel: Magnesiumsalze der Speisefettsäuren, Überzugsmittel: Hydroxypropylmethylcellulose, Eichhase-Extrakt (Polyporus umbellatus; 30 % Polysaccharide), Zinkgluconat, Bambussprossen-Extrakt 5:1 (75 % Silizium), Kupfergluconat, Calcium-D-pantothenat, Pyridoxinhydrochlorid, D-Biotin.<br><b>Verzehrempfehlung:</b> 2 Kapseln täglich mit reichlich Flüssigkeit einnehmen.</p>
    <p><b>Hinweiß:</b><br>Außerhalb der Reichweite von Kindern aufbewahren.</p>
    <p>Die angegebene empfohlene tägliche Verzehrsmenge darf nicht überschritten werden. Kein Ersatz für eine ausgewogene und abwechslungsreiche Ernährung.</p>
    <div class="maker"><span>Hergestellt für:</span><span>Velmarin Versand GmbH<br>Lindenhofweg 7<br>79000 Musterstadt</span></div>
  </section>

  <div class="band">60 KAPSELN = 210g</div>
</main>
</body>
</html>
```